Business Card Design for Photographer

Updating business card design. Must use included logo. We're a luxury wedding photography business. Elegancy, luxury, consistency are messages we wish to convey.

Visit our website at www.colbyvarnway.com to familiarize yourself more with our brand design currently (fonts, colors etc.). This is what we want to maintain.

Target Market(s)

Luxury Brides and Grooms

Industry/Entity Type

Wedding

Contact Information for Business Card

Current logo (attached to brief)
Name: Colby Varnway
Phone: 5208813047
website/blog
Email

Requirements
Must have
• Current logo (attached to brief)
• Name: Colby Varnway
• Phone: 5208813047
• website/blog
• Email
• Instagram username
Should not have
• bright colors, fonts that don't suit our brand (visit www.colbyvarnway.com)

```html
<!DOCTYPE html>
<html lang="en">
<head>
<meta charset="utf-8">
<title>Colby Varnway Photographers — Business Card</title>
<link href="https://fonts.googleapis.com/css2?family=Tenor+Sans&family=Open+Sans:wght@400&display=swap" rel="stylesheet">
<style>
  :root {
    --backdrop: #7d8796;
    --card-front: #ffffff;
    --card-back: #777777;
    --ink-grey: #8a8a8a;
    --ink-white: #ffffff;
    --shadow: rgba(20, 28, 40, 0.28);
  }
  * { box-sizing: border-box; margin: 0; padding: 0; }
  html, body { width: 1200px; height: 1023px; overflow: hidden; }
  body {
    background: var(--backdrop);
    display: flex;
    flex-direction: column;
    align-items: center;
    justify-content: center;
    gap: 63px;
    font-family: "Open Sans", sans-serif;
  }
  .card {
    width: 700px;
    height: 400px;
    display: flex;
    flex-direction: column;
    align-items: center;
    justify-content: center;
    box-shadow: 0 12px 30px var(--shadow);
  }
  .card--front { background: var(--card-front); color: var(--ink-grey); }
  .card--back { background: var(--card-back); color: var(--ink-white); }

  .brand { display: flex; align-items: center; gap: 22px; }
  .brand__square { width: 74px; height: 74px; background: currentColor; flex: none; }
  .brand__text { display: flex; flex-direction: column; }
  .brand__name {
    font-family: "Tenor Sans", sans-serif;
    font-size: 34px;
    letter-spacing: 0.16em;
    text-transform: uppercase;
    line-height: 1.1;
  }
  .brand__tagline {
    font-family: "Tenor Sans", sans-serif;
    font-size: 15px;
    letter-spacing: 0.62em;
    text-transform: uppercase;
    margin-top: 8px;
  }

  .contact {
    margin-top: 44px;
    display: flex;
    flex-direction: column;
    align-items: center;
    gap: 10px;
    font-size: 15px;
  }
  .contact__row { display: flex; align-items: center; gap: 12px; }
  .contact__item { display: flex; align-items: center; gap: 6px; }
  .contact__sep { width: 5px; height: 5px; background: currentColor; }
  .contact__icon { width: 13px; height: 13px; fill: currentColor; }
</style>
</head>
<body>
  <section class="card card--front" aria-label="Business card front">
    <div class="brand">
      <span class="brand__square"></span>
      <div class="brand__text">
        <span class="brand__name">Colby Varnway</span>
        <span class="brand__tagline">Photographers</span>
      </div>
    </div>
    <div class="contact">
      <div class="contact__row">
        <span class="contact__item">
          <svg class="contact__icon" viewBox="0 0 16 16" aria-hidden="true"><path d="M3.5 1.5l2.5 3-1.5 1.8c.9 1.9 2.3 3.3 4.2 4.2L10.5 9l3 2.5-1.5 2.5C6.5 14 2 9.5 1.5 3.5z"/></svg>
          5208813047
        </span>
        <span class="contact__sep"></span>
        <span class="contact__item">
          <svg class="contact__icon" viewBox="0 0 16 16" aria-hidden="true"><rect x="1" y="1" width="14" height="14" rx="2"/></svg>
          colbyvarnwayphoto
        </span>
      </div>
      <div class="contact__row">
        <span class="contact__item">
          <svg class="contact__icon" viewBox="0 0 16 16" aria-hidden="true"><path d="M1 3h14v10H1z M1.5 3.5L8 9l6.5-5.5" fill="none" stroke="currentColor" stroke-width="1.4"/></svg>
          colby@colbyvarnway.com
        </span>
        <span class="contact__sep"></span>
        <span class="contact__item">
          <svg class="contact__icon" viewBox="0 0 16 16" aria-hidden="true"><circle cx="8" cy="8" r="6.5" fill="none" stroke="currentColor" stroke-width="1.4"/><path d="M1.5 8h13M8 1.5c-3 3.5-3 9.5 0 13M8 1.5c3 3.5 3 9.5 0 13" fill="none" stroke="currentColor" stroke-width="1.1"/></svg>
          www.colbyvarnway.com
        </span>
      </div>
    </div>
  </section>

  <section class="card card--back" aria-label="Business card back">
    <div class="brand">
      <span class="brand__square"></span>
      <div class="brand__text">
        <span class="brand__name">Colby Varnway</span>
        <span class="brand__tagline">Photographers</span>
      </div>
    </div>
  </section>
</body>
</html>
```